Brix2Key Header

I want a professional Letterhead for my law firm. I'm attaching the letterhead I currently use in Word and PDF form. I'm also attaching my logo, and an example header that I like.

```html
<!DOCTYPE html>
<html lang="en">
<head>
<meta charset="utf-8">
<title>Brix2Key Letterhead</title>
<link href="https://fonts.googleapis.com/css2?family=Open+Sans:wght@400;600;800&display=swap" rel="stylesheet">
<style>
  :root {
    --backdrop: #d8c9ad;
    --paper: #ffffff;
    --ink: #3a3a3a;
    --muted: #6a6a6a;
    --brand-blue: #1f6fbd;
    --brand-green: #5e9f4a;
    --brand-dark: #2b2b2b;
  }
  * { box-sizing: border-box; margin: 0; padding: 0; }
  html, body {
    width: 1200px; height: 898px; overflow: hidden;
    background: var(--backdrop);
    font-family: "Open Sans", Arial, sans-serif;
    color: var(--ink);
  }
  .letterhead {
    position: absolute; left: 300px; top: 24px;
    width: 600px; height: 850px;
    background: var(--paper);
    box-shadow: 0 6px 24px rgba(0,0,0,0.12);
  }
  .brand {
    position: absolute; left: 46px; top: 114px;
    display: flex; align-items: center; gap: 8px;
  }
  .brand-mark { width: 12px; height: 12px; background: var(--brand-blue); }
  .brand-name {
    font-weight: 800; font-size: 28px; letter-spacing: 0.5px;
    color: var(--brand-dark); line-height: 1;
  }
  .sender {
    position: absolute; left: 232px; top: 76px;
    border-left: 2px solid var(--brand-blue);
    padding: 4px 0 10px 12px;
    font-size: 8.5px; line-height: 15px; color: var(--muted);
    font-style: normal;
  }
  .contacts {
    position: absolute; left: 424px; top: 58px;
    border-left: 2px solid var(--brand-green);
    padding: 2px 0 4px 10px;
    font-size: 8px; line-height: 14px; color: var(--muted);
    list-style: none;
  }
  .contacts li { display: flex; align-items: center; gap: 6px; }
  .icon { width: 8px; height: 8px; fill: var(--brand-blue); flex: none; }
  .date {
    position: absolute; right: 54px; top: 138px;
    font-size: 10px; color: var(--muted);
  }
  .recipient {
    position: absolute; left: 64px; top: 250px;
    font-size: 11px; line-height: 17px; color: var(--muted);
    font-style: normal;
  }
  .letter-body {
    position: absolute; left: 64px; top: 334px; width: 476px;
    font-size: 10.5px; line-height: 17px; color: var(--ink);
  }
  .salutation { margin-bottom: 10px; color: var(--muted); }
  .letter-body p + p { margin-top: 16px; }
  .closing {
    position: absolute; left: 412px; top: 676px;
    font-size: 10px; color: var(--ink);
  }
  .signature {
    display: block; margin-top: 6px;
    width: 110px; height: 40px; border-radius: 4px;
    background: linear-gradient(90deg, rgba(31,111,189,0.08), rgba(31,111,189,0.2), rgba(31,111,189,0.08));
  }
  .footer-contacts {
    position: absolute; left: 40px; right: 40px; top: 752px;
    display: flex; justify-content: space-between;
    font-size: 7.5px; color: var(--muted);
    list-style: none;
  }
  .footer-contacts li { display: flex; align-items: center; gap: 4px; }
  .footer-band {
    position: absolute; left: 0; right: 0; bottom: 34px; height: 40px;
    background: repeating-linear-gradient(90deg, var(--brand-blue) 0 2px, #2a7cc8 2px 3px);
    border-top: 2px solid var(--brand-green);
  }
  .footer-tagline {
    position: absolute; right: 150px; top: 8px;
    font-size: 16px; color: #fff; letter-spacing: 0.5px;
  }
</style>
</head>
<body>
  <article class="letterhead">
    <div class="brand">
      <span class="brand-mark"></span>
      <span class="brand-name">Brix2Key</span>
    </div>

    <address class="sender">
      Marcus T. Delgado III, Attorney at law, PLLC<br>
      2410 Harwell avenue suite 200<br>
      Austin, Texas 78701
    </address>

    <ul class="contacts">
      <li><svg class="icon" viewBox="0 0 10 10"><path d="M1 3c0-1 1-2 4-2s4 1 4 2v1H7V3H3v1H1zM2 5h6l1 4H1z"/></svg>(512) 555-0148</li>
      <li><svg class="icon" viewBox="0 0 10 10"><path d="M2 1h6v3H2zM0 4h10v4H8V6H2v2H0zM3 7h4v3H3z"/></svg>(888) 555-0193</li>
      <li><svg class="icon" viewBox="0 0 10 10"><path d="M1 1l8 3-3 1-1 4z"/></svg>team.brix2key.com</li>
      <li><svg class="icon" viewBox="0 0 10 10"><circle cx="5" cy="5" r="4.5"/></svg>www.brix2key.com</li>
    </ul>

    <p class="date">September 14, 2021</p>

    <address class="recipient">
      Dear Mrs. Jane Rowe<br>
      Managing Director<br>
      2410 Harwell avenue suite 200<br>
      Austin, Texas 78701
    </address>

    <section class="letter-body">
      <p class="salutation">Dear Customer,</p>
      <p>Lorem ipsum dolor sit amet, consectetur adipiscing elit. Donec orci purus, luctus vitae dignissim eu, iaculis sed purus. Vivamus faucibus, ipsum nec aliquet viverra, leo mauris condimentum ligula, sit amet sagittis enim ligula quis arcu. Nam egestas tortor id nisi porttitor mattis. In tortor ante, ultricies in suscipit a, tempus non massa. Vivamus et auctor mi. Fusce vel massa nulla. Phasellus nec eros mauris, et scelerisque orci.</p>
      <p>Donec malesuada orci vitae nulla accumsan porta a id massa. Quisque accumsan iaculis magna sit amet fringilla. Maecenas consequat, magna eget tincidunt semper, odio nibh rutrum mi, id feugiat ante nisi eu risus. Vestibulum nunc orci, rhoncus a placerat in, ultricies in mi. Cras mattis varius eros, vel fringilla nisi suscipit eget. Quisque scelerisque sagittis nulla at porttitor.</p>
      <p>Sed id augue vitae urna euismod commodo aliquet a quam. Pellentesque arcu velit, cursus et malesuada ut, consequat et diam. Nullam erat sem, rhoncus id ullamcorper vitae, rhoncus et arcu. In ultricies ultricies nulla, ut rutrum nisi iaculis at. Donec eu magna a metus ornare faucibus. Fusce aliquet faucibus ultricies. Morbi semper, est id tincidunt gravida, sem arcu adipiscing lacus, ac bibendum nulla leo eu purus. Quisque nec diam sed risus consectetur a ccumsan quis quis nibh. Vestibulum id purus lorem.</p>
    </section>

    <div class="closing">
      Sincerely,
      <span class="signature" role="img" aria-label="Handwritten signature of the attorney"></span>
    </div>

    <ul class="footer-contacts">
      <li><svg class="icon" viewBox="0 0 10 10"><path d="M5 1l4 4H8v4H2V5H1z"/></svg>2410 Harwell avenue suite 200 Austin, Texas 78701</li>
      <li><svg class="icon" viewBox="0 0 10 10"><path d="M1 3c0-1 1-2 4-2s4 1 4 2v1H7V3H3v1H1zM2 5h6l1 4H1z"/></svg>(512) 555-0148</li>
      <li><svg class="icon" viewBox="0 0 10 10"><path d="M2 1h6v3H2zM0 4h10v4H8V6H2v2H0zM3 7h4v3H3z"/></svg>(888) 555-0193</li>
      <li><svg class="icon" viewBox="0 0 10 10"><path d="M1 1l8 3-3 1-1 4z"/></svg>team.brix2key.com</li>
      <li><svg class="icon" viewBox="0 0 10 10"><circle cx="5" cy="5" r="4.5"/></svg>www.brix2key.com</li>
    </ul>

    <div class="footer-band">
      <span class="footer-tagline">Turn The Key</span>
    </div>
  </article>
</body>
</html>
```